CD cover

It's about a music CD.
Artist: COPPER AND KIN
Title: HARBOR GLOW
Style: jazz-pop
Ideas: dancing flowers, something playful, something beautiful
possible elements: flowers, music, oriental shapes, something colorful

Target Market(s)

Music consumers from Tunevale and Co.

Industry/Entity Type

Musik

Requirements
Nice to have
• Attached are two examples (dancing flowers)

```html
<!DOCTYPE html>
<html lang="en">
<head>
<meta charset="utf-8">
<title>Copper and Kin – Harbor Glow</title>
<link rel="stylesheet" href="https://fonts.googleapis.com/css2?family=Luckiest+Guy&family=Bree+Serif&display=swap">
<style>
  :root {
    --night: #292a40;
    --gold-light: #fbe9a0;
    --gold-mid: #d9a93a;
    --gold-deep: #8a5a16;
    --berry: #a8174f;
    --crimson: #c8133a;
    --leaf: #62a33f;
    --cobalt: #3b5ba8;
    --violet: #9c4a96;
    --lime: #b9cc5a;
    --sky: #6fb8ea;
    --cream: #f6f0b0;
    --white: #ffffff;
  }
  html, body {
    margin: 0;
    padding: 0;
    width: 1200px;
    height: 1200px;
    overflow: hidden;
    background: var(--night);
  }
  .cover {
    position: relative;
    width: 1200px;
    height: 1200px;
    background: var(--night);
    overflow: hidden;
  }
  .flower-field {
    position: absolute;
    inset: 0;
    background:
      radial-gradient(circle at 22% 20%, rgba(59, 91, 168, 0.55) 0, rgba(59, 91, 168, 0) 22%),
      radial-gradient(circle at 55% 12%, rgba(185, 204, 90, 0.45) 0, rgba(185, 204, 90, 0) 20%),
      radial-gradient(circle at 88% 28%, rgba(200, 19, 58, 0.55) 0, rgba(200, 19, 58, 0) 22%),
      radial-gradient(circle at 8% 40%, rgba(190, 220, 195, 0.35) 0, rgba(190, 220, 195, 0) 16%),
      radial-gradient(circle at 10% 62%, rgba(220, 110, 170, 0.40) 0, rgba(220, 110, 170, 0) 15%),
      radial-gradient(circle at 28% 56%, rgba(240, 225, 50, 0.40) 0, rgba(240, 225, 50, 0) 14%),
      radial-gradient(circle at 62% 42%, rgba(200, 110, 30, 0.40) 0, rgba(200, 110, 30, 0) 18%),
      radial-gradient(circle at 45% 78%, rgba(168, 23, 79, 0.60) 0, rgba(168, 23, 79, 0) 28%),
      radial-gradient(circle at 78% 68%, rgba(98, 163, 63, 0.60) 0, rgba(98, 163, 63, 0) 26%),
      radial-gradient(circle at 16% 86%, rgba(156, 74, 150, 0.55) 0, rgba(156, 74, 150, 0) 20%),
      radial-gradient(circle at 80% 96%, rgba(111, 184, 234, 0.50) 0, rgba(111, 184, 234, 0) 18%),
      var(--night);
  }
  .artist {
    position: absolute;
    left: 0;
    top: 175px;
    width: 1200px;
    margin: 0;
    text-align: center;
    font-family: "Luckiest Guy", "Arial Black", sans-serif;
    font-weight: 400;
    line-height: 1;
    transform: rotate(3deg);
  }
  .artist-line {
    display: block;
    background: linear-gradient(180deg, var(--gold-light) 0%, var(--gold-mid) 45%, var(--gold-deep) 75%, var(--gold-mid) 100%);
    -webkit-background-clip: text;
    background-clip: text;
    color: transparent;
    filter: drop-shadow(0 6px 8px rgba(0, 0, 0, 0.55));
    letter-spacing: 4px;
  }
  .artist-line--big {
    font-size: 150px;
  }
  .artist-line--small {
    font-size: 82px;
    margin: 4px 0 6px;
  }
  .album-title {
    position: absolute;
    left: 0;
    top: 1048px;
    width: 1200px;
    margin: 0;
    text-align: center;
    font-family: "Bree Serif", Georgia, serif;
    font-size: 92px;
    font-weight: 400;
    color: var(--white);
    letter-spacing: 2px;
    -webkit-text-stroke: 4px var(--berry);
    paint-order: stroke fill;
    text-shadow: 0 5px 10px rgba(0, 0, 0, 0.5);
  }
</style>
</head>
<body>
  <main class="cover">
    <div class="flower-field" role="img" aria-label="Playful scattered flowers with rounded teardrop petals in blue, lime, red, pink, yellow, berry, green, violet and sky blue, each with a pale cream centre"></div>
    <h1 class="artist">
      <span class="artist-line artist-line--big">COPPER</span>
      <span class="artist-line artist-line--small">AND</span>
      <span class="artist-line artist-line--big">KIN</span>
    </h1>
    <h2 class="album-title">Harbor Glow</h2>
  </main>
</body>
</html>
```